Business Card - Harlow Birch

Need Business Card design for company named Harlow Birch. Software development focused mainly on Ardel eKallo & oBix Apps. I've attached our logo with both a black and white background. Please add trademark symbol to logo when using.

```html
<!DOCTYPE html>
<html lang="en">
<head>
<meta charset="utf-8">
<title>Harlow Birch — Business Card</title>
<link rel="stylesheet" href="https://fonts.googleapis.com/css2?family=Inter:wght@400;500;700&display=swap">
<style>
  :root {
    --page-bg: #ffffff;
    --ink: #111111;
    --card-dark: #101415;
    --text-light: #ffffff;
    --accent-orange: #f98b00;
    --accent-red: #e30000;
    --label-red: #d42a1c;
    --label-orange: #f07a1a;
    --label-yellow: #f5b400;
  }
  * { margin: 0; padding: 0; box-sizing: border-box; }
  html, body {
    width: 1200px;
    height: 900px;
    overflow: hidden;
    background: var(--page-bg);
    font-family: "Inter", Helvetica, Arial, sans-serif;
  }
  .sheet { position: relative; width: 1200px; height: 900px; }
  .side-label {
    position: absolute;
    top: 210px;
    font-size: 16px;
    font-weight: 700;
    color: var(--ink);
    letter-spacing: 0.2px;
  }
  .side-label--front { left: 38px; }
  .side-label--back { left: 616px; }

  .card {
    position: absolute;
    top: 283px;
    width: 546px;
    height: 311px;
    overflow: hidden;
  }
  .card--front { left: 38px; background: var(--card-dark); }
  .card--back {
    left: 616px;
    background: linear-gradient(90deg, var(--accent-orange) 0%, var(--accent-orange) 12%, var(--accent-red) 100%);
  }

  .brand {
    position: absolute;
    left: 40px;
    top: 66px;
    display: flex;
    flex-direction: column;
    gap: 14px;
  }
  .brand-dot {
    width: 34px;
    height: 34px;
    border-radius: 50%;
    background: var(--accent-orange);
  }
  .brand-name {
    font-size: 22px;
    font-weight: 700;
    color: var(--text-light);
    letter-spacing: -0.6px;
    line-height: 1;
  }

  .contact-person, .contact-lines {
    position: absolute;
    top: 208px;
    color: var(--text-light);
    font-size: 15px;
    line-height: 24px;
  }
  .contact-person { left: 155px; }
  .person-name { font-weight: 700; font-size: 16px; letter-spacing: 0.6px; }
  .contact-lines { left: 345px; }
  .contact-row { display: flex; align-items: baseline; }
  .contact-key {
    display: inline-block;
    width: 30px;
    font-size: 10px;
    text-align: center;
  }
  .contact-key--mobile { color: var(--label-red); }
  .contact-key--fax { color: var(--label-orange); }
  .contact-key--email { color: var(--label-yellow); }

  .back-name {
    position: absolute;
    inset: 0;
    display: flex;
    align-items: center;
    justify-content: center;
    padding-top: 8px;
    font-size: 42px;
    font-weight: 700;
    color: var(--text-light);
    letter-spacing: -1.4px;
  }
</style>
</head>
<body>
<main class="sheet">
  <h2 class="side-label side-label--front">Front</h2>
  <h2 class="side-label side-label--back">Back</h2>

  <section class="card card--front" aria-label="Card front">
    <div class="brand">
      <span class="brand-dot" aria-hidden="true"></span>
      <span class="brand-name">Harlow Birch</span>
    </div>
    <div class="contact-person">
      <p class="person-name">Dale Morrow</p>
      <p>4820 Larkspur Rd</p>
      <p>Tamsin, FL 33690</p>
    </div>
    <div class="contact-lines">
      <p class="contact-row"><span class="contact-key contact-key--mobile">{m}</span>555-214-9900</p>
      <p class="contact-row"><span class="contact-key contact-key--fax">{f}</span>555-214-2725</p>
      <p class="contact-row"><span class="contact-key contact-key--email">{e}</span>D.Morrow@HB.com</p>
    </div>
  </section>

  <section class="card card--back" aria-label="Card back">
    <p class="back-name">Harlow Birch</p>
  </section>
</main>
</body>
</html>
```